TV+Music+Social Network+Entertainment+brightlistin= Designers lol

TV+ Music+ Social Network +Entertainment+ brightlistin=

ZELLOPAK.COM

Zellopak is a one-stop shop promotional plateform that will communicate information to all user of what is COOL, NEW and Exicting in your Neighborhood.(News,Events,Entertainment,ect) We promote for all User/Entrepreneur/business/Talents.We are the future and dream destination for all to whom owns a computer. Forming the the World Wide Web into your Local Wide Web. (Atlanta, Dallas, Las Vegas, New York ect.)

* EX: ( WWW. ??? .com =LWW. ??? .com)
WORLD = LOCAL

* Goal/Mission: Have customer/user visit the website and then leave their house to go experience life in their respective surroundings.

/////////////////////////Web page///////////////////////

Colors:Blue/Green/black

include: interchangable background picture @ top (to update easily and keep fresh) On this background picture include logo (top left) login/sign (top left)

Major Tabs: Music/Daylife/Nightlife/Video/Shop

Industry/Entity Type

House

Requirements
Nice to have
• Tv screen/search engine

```html
<!DOCTYPE html>
<html lang="en">
<head>
<meta charset="utf-8">
<title>Zellopak</title>
<link rel="stylesheet" href="https://fonts.googleapis.com/css2?family=Open+Sans:wght@400;600&display=swap">
<style>
:root{
  --bg:#0b0c0e;
  --panel:#1c1c1d;
  --panel-inner:#232323;
  --box:#2b2b2b;
  --line:#3a3a3a;
  --green:#7bb63a;
  --text:#a8a8a8;
  --link:#3f8de0;
  --blue-deep:#04132e;
  --blue-mid:#0c2f70;
  --social:#1a4f96;
}
*{margin:0;padding:0;box-sizing:border-box}
html,body{width:900px;height:1200px;overflow:hidden;background:var(--bg)}
body{position:relative;font-family:"Open Sans",Arial,sans-serif;color:var(--text)}
.abs{position:absolute}

.header-scene{left:0;top:0;width:900px;height:200px;
  background:linear-gradient(180deg,#060b16 0%,var(--blue-deep) 40%,var(--blue-mid) 72%,#081630 88%,var(--bg) 100%)}
.brand{left:66px;top:30px;display:flex;align-items:center;gap:10px}
.brand-dot{width:50px;height:50px;border-radius:50%;background:#2f79d6}
.brand-name{font-size:40px;font-weight:400;color:#fff;line-height:1}

.search{left:266px;top:117px;width:384px;height:44px;border-radius:8px 8px 0 0;
  background:linear-gradient(#4a4a4a,#2a2a2a);padding:8px 8px 0}
.search-field{height:26px;border-radius:4px;background:#1a1a1a;border:1px solid #000;
  font-size:11px;color:#bbb;text-align:right;padding:5px 10px 0}

.nav{left:85px;top:159px;width:745px;height:38px;border-radius:8px;
  background:linear-gradient(#404040,#1e1e1e 60%,#151515)}
.nav a{position:absolute;top:13px;font-size:10.5px;color:#ddd;text-decoration:none}
.nav a.active{color:#fff;font-weight:600}
.nav .sep{position:absolute;top:0;width:1px;height:38px;background:#111;box-shadow:1px 0 0 #454545}

.hero{left:85px;top:205px;width:745px;height:257px;border:3px solid #222;background:#000}
.hero-photo{position:absolute;inset:0;
  background:linear-gradient(180deg,#123a5e 0%,#0a1d33 45%,#081421 70%,#020406 100%)}
.hero-pager{position:absolute;left:320px;bottom:0;width:130px;height:22px;border-radius:10px 10px 0 0;
  background:linear-gradient(#4a4a4a,#222);display:flex;justify-content:center;align-items:center;gap:10px}
.hero-pager i{width:8px;height:8px;border-radius:50%;background:#111}
.hero-pager i.on{background:#eee}

.social{left:33px;top:233px;width:42px;height:165px;border-radius:4px 0 0 4px;background:var(--social);
  display:flex;flex-direction:column;align-items:center;gap:14px;padding-top:10px}
.social i{width:19px;height:19px;border-radius:50%;background:#fff}
.social-tip{left:75px;top:243px}

.rail-line{left:848px;top:228px;width:1px;height:890px;background:#555}
.rail-knob{left:841px;top:281px;width:15px;height:15px;border-radius:50%;background:radial-gradient(circle at 40% 35%,#ccc,#666)}

.content{left:85px;top:465px;width:745px;height:678px;background:var(--panel)}
.content-inner{left:93px;top:474px;width:728px;height:660px;background:var(--panel-inner)}

h2{font-weight:400;color:var(--green);font-size:17px;letter-spacing:.2px}
.dots{height:1px;border-top:1px dotted #6e6e6e}
.rule{height:1px;background:var(--line)}
p.body{font-size:9.1px;line-height:19px}

.event-title{font-size:13.5px;color:#c9c9c9}
.event-text{font-size:9.3px;line-height:17px;text-align:justify;width:263px}
.event-photo{width:199px;height:163px;border-radius:3px;
  background:linear-gradient(180deg,#7466c4,#3c2d6a 55%,#6a3a92 85%,#2a1a3a)}
.more{font-size:10px;color:var(--link)}

.pager{font-size:10.5px;color:#bbb;word-spacing:1px}
.pager b{color:#fff;font-weight:600}

.side-box{left:608px;width:204px;background:var(--box)}
.side-box h2{position:absolute;left:13px;font-size:13.5px}
.side-box .dots{position:absolute;left:13px;right:10px}
.item{position:absolute;left:7px;display:flex;gap:9px}
.thumb{width:63px;height:53px;border:1px solid #444;background:linear-gradient(135deg,#3b4a5e,#151a22)}
.item p{width:113px;font-size:9.3px;line-height:13.8px;text-align:justify}

.news-input{left:620px;top:1064px;width:181px;height:26px;background:linear-gradient(#d8d8d8,#bdbdbd)}
.submit{left:753px;top:1096px;width:48px;height:18px;background:var(--green);color:#102;font-size:10px;text-align:center;line-height:18px}

.footer{width:775px;text-align:center;font-size:10px;color:#bbb}
.footer span{margin:0 5px;color:#888}
</style>
</head>
<body>

<div class="abs header-scene" role="img" aria-label="Changeable header photo: night landscape under a blue sky"></div>
<div class="abs brand"><span class="brand-dot"></span><span class="brand-name">zellopak</span></div>

<div class="abs search"><div class="search-field">SEARCH</div></div>

<nav class="abs nav">
  <a class="active" style="left:183px">MUSIC</a>
  <span class="sep" style="left:237px"></span>
  <a style="left:262px">VIDEOS</a>
  <span class="sep" style="left:325px"></span>
  <a style="left:348px">NIGHT LIFE</a>
  <span class="sep" style="left:426px"></span>
  <a style="left:449px">DAY LIFE</a>
  <span class="sep" style="left:512px"></span>
  <a style="left:539px">SHOP</a>
</nav>

<div class="abs hero">
  <div class="hero-photo" role="img" aria-label="Concert crowd in front of a stage lit by blue lights"></div>
  <div class="hero-pager"><i class="on"></i><i></i><i></i><i></i></div>
</div>

<div class="abs social"><i></i><i></i><i></i><i></i><i></i></div>
<svg class="abs social-tip" width="10" height="18" viewBox="0 0 10 18"><path d="M0 0L10 9L0 18Z" fill="#1a4f96"/></svg>

<svg class="abs" style="left:837px;top:205px" width="24" height="16" viewBox="0 0 24 16"><path d="M3 13L12 4L21 13" fill="none" stroke="#777" stroke-width="4"/></svg>
<div class="abs rail-line"></div>
<div class="abs rail-knob"></div>
<svg class="abs" style="left:837px;top:1124px" width="24" height="16" viewBox="0 0 24 16"><path d="M3 3L12 12L21 3" fill="none" stroke="#777" stroke-width="4"/></svg>

<div class="abs content"></div>
<div class="abs content-inner"></div>

<h2 class="abs" style="left:106px;top:492px">WELCOME TO OUR SITE</h2>
<div class="abs dots" style="left:106px;top:524px;width:486px"></div>
<p class="abs body" style="left:106px;top:533px;width:488px">Sed ut perspiciatis unde omnis iste natus error sit voluptatem accusantium doloremque laudantium, totam rem aperiam, eaque ipsa quae ab illo inventore veritatis et quasi architecto beatae vitae dicta sunt explicabo. Nemo enim ipsam voluptatem quia voluptas sit aspernatur aut odit aut fugit, sed quia consequuntur magni dolores eos qui ratione voluptatem sequi nesciunt.</p>
<div class="abs rule" style="left:106px;top:624px;width:486px"></div>

<h2 class="abs" style="left:106px;top:638px">LATEST EVENTS</h2>
<div class="abs dots" style="left:106px;top:670px;width:486px"></div>

<div class="abs event-title" style="left:106px;top:690px">Quis autem vel eum iure reprehenderit</div>
<p class="abs event-text" style="left:106px;top:718px">Sed ut perspiciatis unde omnis iste natus error sit voluptatem accusantium doloremque laudantium, totam rem aperiam, eaque ipsa quae ab illo inventore veritatis et quasi architecto beatae vitae dicta sunt explicabo. Nemo enim ipsam voluptatem quia voluptas sit aspernatur aut odit aut fugit, sed quia consequuntur magni dolores eos qui ratione voluptatem sequi nesciunt.</p>
<div class="abs event-photo" style="left:386px;top:692px" role="img" aria-label="Concert hall with stage truss and purple lighting"></div>
<a class="abs more" style="left:317px;top:845px">View more</a>
<div class="abs rule" style="left:106px;top:874px;width:486px"></div>

<div class="abs event-title" style="left:106px;top:891px">Quis autem vel eum iure reprehenderit</div>
<p class="abs event-text" style="left:106px;top:919px">Sed ut perspiciatis unde omnis iste natus error sit voluptatem accusantium doloremque laudantium, totam rem aperiam, eaque ipsa quae ab illo inventore veritatis et quasi architecto beatae vitae dicta sunt explicabo. Nemo enim ipsam voluptatem quia voluptas sit aspernatur aut odit aut fugit, sed quia consequuntur magni dolores eos qui ratione voluptatem sequi nesciunt.</p>
<div class="abs event-photo" style="left:386px;top:893px" role="img" aria-label="Concert hall with stage truss and purple lighting"></div>
<a class="abs more" style="left:317px;top:1046px">View more</a>
<div class="abs rule" style="left:106px;top:1075px;width:486px"></div>

<div class="abs pager" style="left:364px;top:1097px">&lt;&lt; &nbsp; <b>1</b> / 2 / 3 / 4 / 5 / 6 . . . . . 28 / 29 / 30 &nbsp; &gt;&gt;</div>

<section class="abs side-box" style="top:483px;height:262px">
  <h2 style="top:10px">LATEST NEWS</h2>
  <div class="dots" style="top:41px"></div>
  <div class="item" style="top:55px"><div class="thumb" role="img" aria-label="Party crowd photo"></div><p>sed quia consequuntur magni dolores eos qui ratione voluptatem sequi nesciunt.</p></div>
  <div class="item" style="top:125px"><div class="thumb" style="background:linear-gradient(#2e7fd0,#9cc8ef)" role="img" aria-label="Basketball player dunking"></div><p>sed quia consequuntur magni dolores eos qui ratione voluptatem sequi nesciunt.</p></div>
  <div class="item" style="top:194px"><div class="thumb" style="background:linear-gradient(135deg,#ddd,#555)" role="img" aria-label="Bike rider on a ramp"></div><p>sed quia consequuntur magni dolores eos qui ratione voluptatem sequi nesciunt.</p></div>
</section>

<section class="abs side-box" style="top:755px;height:262px">
  <h2 style="top:10px">ENTERTAINMENT</h2>
  <div class="dots" style="top:41px"></div>
  <div class="item" style="top:56px"><div class="thumb" style="background:linear-gradient(135deg,#bbb,#222)" role="img" aria-label="Movie still"></div><p>sed quia consequuntur magni dolores eos qui ratione voluptatem sequi nesciunt.</p></div>
  <div class="item" style="top:125px"><div class="thumb" style="background:linear-gradient(135deg,#3a6d9a,#1a2a3a)" role="img" aria-label="Film character still"></div><p>sed quia consequuntur magni dolores eos qui ratione voluptatem sequi nesciunt.</p></div>
  <div class="item" style="top:195px"><div class="thumb" style="background:linear-gradient(135deg,#6a5a50,#1a1614)" role="img" aria-label="Fitness photo"></div><p>sed quia consequuntur magni dolores eos qui ratione voluptatem sequi nesciunt.</p></div>
</section>

<section class="abs side-box" style="top:1028px;height:96px">
  <h2 style="top:8px">NEWS LETTER SIGNUP</h2>
</section>
<div class="abs news-input"></div>
<div class="abs submit">SUBMIT</div>

<div class="abs footer" style="left:64px;top:1155px">Music<span>|</span>Videos<span>|</span>Night Life<span>|</span>Day Life<span>|</span>Shop</div>
<div class="abs footer" style="left:64px;top:1177px">Copyright © 2012 Zellopak &nbsp;&nbsp;&nbsp; All rights reserved</div>

</body>
</html>
```